Business Cards & Letterhead etc.
Would like our Business Cards designed off our Logo
Professional
Dale Fenwick
PO Box 61309
Macon, GA 31987
fenwickd@quellbridgeco.com
www.quellbridgeco.com
I would like the business cards to be designed so i can later alter the contact info for multiple people. Anything in Adobe is fine.

```html
<!DOCTYPE html>
<html lang="en">
<head>
<meta charset="utf-8">
<title>Quell IT Group – Business Cards</title>
<link href="https://fonts.googleapis.com/css2?family=Arimo:wght@400;700&display=swap" rel="stylesheet">
<style>
  :root {
    --board: #000000;
    --white: #ffffff;
    --brand-blue: #1f8fd6;
    --brand-navy: #0d3a6e;
    --sky-light: #3cc3f0;
    --sky-dark: #0a5f9c;
    --grey-light: #d4d4d4;
    --grey-dark: #6e6e6e;
    --ink: #1a1a1a;
    --mark: #4a7fae;
  }
  * { margin: 0; padding: 0; box-sizing: border-box; }
  html, body { width: 1200px; height: 722px; overflow: hidden; background: var(--board); }
  body { font-family: "Arimo", Arial, sans-serif; position: relative; }

  .card {
    position: absolute;
    width: 500px;
    height: 284px;
    border-radius: 26px;
    overflow: hidden;
  }
  .card--front { left: 91px; top: 72px; background: var(--white); }
  .card--blue  { left: 614px; top: 72px; background: radial-gradient(ellipse at 20% 0%, var(--sky-light), var(--sky-dark) 90%); }
  .card--white { left: 91px; top: 380px; background: var(--white); }
  .card--grey  { left: 614px; top: 380px; background: linear-gradient(100deg, var(--grey-light), var(--grey-dark)); }

  .front-swoosh { position: absolute; left: 0; top: 0; width: 500px; height: 120px; }

  .brand {
    position: absolute;
    left: 16px;
    top: 22px;
    display: flex;
    align-items: center;
    gap: 10px;
  }
  .brand__dot { width: 46px; height: 46px; border-radius: 50%; background: var(--mark); flex: none; }
  .brand__name {
    font-weight: 700;
    font-size: 22px;
    line-height: 22px;
    color: var(--brand-navy);
    letter-spacing: 1px;
  }

  .front-faint {
    position: absolute;
    left: 318px;
    top: 96px;
    width: 170px;
    height: 170px;
    border-radius: 50%;
    background: #e9eef3;
  }

  .person { position: absolute; left: 216px; top: 128px; }
  .person__name { font-weight: 700; font-size: 21px; color: var(--brand-blue); }
  .person__role { font-size: 14px; color: var(--ink); margin-top: 2px; padding-left: 50px; }

  .contact {
    position: absolute;
    left: 10px;
    top: 204px;
    font-size: 11.5px;
    line-height: 14.5px;
    color: var(--ink);
  }
  .contact__label { color: var(--brand-blue); }
  .contact__web { color: var(--brand-blue); }

  .emblem {
    position: absolute;
    left: 50%;
    top: 50%;
    transform: translate(-50%, -50%);
    display: flex;
    flex-direction: column;
    align-items: center;
    gap: 10px;
  }
  .emblem__dot { width: 130px; height: 130px; border-radius: 50%; background: var(--mark); }
  .emblem__name { font-weight: 700; font-size: 20px; color: var(--brand-navy); letter-spacing: 1px; }
  .card--blue .emblem__name { color: var(--white); }
</style>
</head>
<body>
  <section class="card card--front">
    <svg class="front-swoosh" viewBox="0 0 500 120" aria-hidden="true">
      <defs>
        <linearGradient id="swoosh-fill" x1="0" y1="0" x2="1" y2="0">
          <stop offset="0" stop-color="#ffffff"/>
          <stop offset="0.55" stop-color="#2b86c8"/>
          <stop offset="1" stop-color="#0d3a6e"/>
        </linearGradient>
      </defs>
      <path d="M0 0 H500 V35 C430 20 400 30 360 70 C330 30 250 35 180 45 C110 50 40 40 0 30 Z" fill="url(#swoosh-fill)"/>
      <path d="M360 70 C395 30 440 22 500 35 V0 H430 C400 10 375 35 360 70 Z" fill="#0d3a6e"/>
      <path d="M395 0 C420 30 455 45 500 48 V0 Z" fill="#dfe4ea"/>
    </svg>
    <div class="brand">
      <span class="brand__dot"></span>
      <span class="brand__name">QUELL<br>IT GROUP</span>
    </div>
    <div class="front-faint" aria-hidden="true"></div>
    <div class="person">
      <div class="person__name">Dale Fenwick</div>
      <div class="person__role">Owner</div>
    </div>
    <div class="contact">
      <div>PO Box 61309, Harlow, KS 66712</div>
      <div><span class="contact__label">Toll free:</span> 866-555-0142 | <span class="contact__label">Cell:</span> 620-555-0187</div>
      <div><span class="contact__label">Fax:</span> 866-555-0163</div>
      <div><span class="contact__label">Email:</span> fenwickd@quellbridgeco.com</div>
      <div class="contact__web">www.quellbridgeco.com</div>
    </div>
  </section>

  <section class="card card--blue">
    <div class="emblem"><span class="emblem__dot"></span><span class="emblem__name">QUELL</span></div>
  </section>

  <section class="card card--white">
    <div class="emblem"><span class="emblem__dot"></span><span class="emblem__name">QUELL</span></div>
  </section>

  <section class="card card--grey">
    <div class="emblem"><span class="emblem__dot"></span><span class="emblem__name">QUELL</span></div>
  </section>
</body>
</html>
```